1923 Basins & Spouts Business Card

I'm wanting to get a business card designed. Our business is 1923 Basins & Spouts
Details for the card:

1923 Basins & Spouts
Name: Gareth Vostle
Email: gareth@1923basinsandspouts.com.au
Website: www.1923basinsandspouts.com.au
Mobile: 0439 602 158
Phone: 02 5550 1843

Font of Basins & Spouts is called Snell Roundhand. Not sue what font logo text is.

I'm thinking two sided but it doesn't have to be.

```html
<!DOCTYPE html>
<html lang="en">
<head>
<meta charset="utf-8">
<title>1923 Basins &amp; Spouts Business Card</title>
<link rel="stylesheet" href="https://fonts.googleapis.com/css2?family=Roboto:wght@400;500&family=Poppins:wght@400&display=swap">
<style>
  :root {
    --backdrop: #e9e9e9;
    --card-light: #ffffff;
    --card-dark-top: #252525;
    --card-dark-bottom: #1b1b1b;
    --ink: #111111;
    --ink-soft: #333333;
    --rule: #a8a8a8;
    --paper-text: #f2f2f2;
  }
  * { margin: 0; padding: 0; box-sizing: border-box; }
  html, body {
    width: 1200px; height: 1200px; overflow: hidden;
    background: var(--backdrop);
  }
  .canvas { position: relative; width: 1200px; height: 1200px; }
  .card { position: absolute; left: 262px; width: 686px; height: 392px; }
  .card-front { top: 165px; background: var(--card-light); color: var(--ink); font-family: "Roboto", Arial, sans-serif; }
  .card-back {
    top: 653px;
    background: linear-gradient(180deg, var(--card-dark-top), var(--card-dark-bottom));
    color: var(--paper-text);
  }
  .brand-lockup { position: absolute; right: 50px; top: 52px; text-align: left; }
  .brand-name { font-size: 22px; font-weight: 400; color: var(--ink); letter-spacing: 0.3px; }
  .brand-tagline { font-size: 8px; color: var(--ink-soft); margin-top: 5px; }
  .holder-name { position: absolute; left: 44px; top: 250px; font-size: 26px; font-weight: 500; }
  .divider { position: absolute; left: 44px; right: 50px; top: 293px; height: 1.5px; background: var(--rule); }
  .contact-list { position: absolute; top: 306px; font-size: 16.5px; line-height: 23px; list-style: none; }
  .contact-list li { display: flex; align-items: center; gap: 9px; }
  .contact-phones { left: 44px; }
  .contact-online { right: 50px; }
  .contact-online li { justify-content: flex-end; }
  .icon { width: 13px; height: 13px; fill: var(--ink); flex: none; }
  .back-brand {
    position: absolute; left: 0; right: 0; top: 160px; text-align: center;
    font-family: "Roboto", Arial, sans-serif; font-size: 36px; font-weight: 400;
  }
  .back-web {
    position: absolute; left: 0; right: 0; top: 322px; text-align: center;
    font-family: "Poppins", Arial, sans-serif; font-size: 16px; letter-spacing: 3px;
  }
</style>
</head>
<body>
<main class="canvas">
  <section class="card card-front">
    <div class="brand-lockup">
      <div class="brand-name">1923 Basins &amp; Spouts</div>
      <div class="brand-tagline">Period elegance crafted for graceful everyday living</div>
    </div>
    <h1 class="holder-name">Gareth Vostle</h1>
    <div class="divider"></div>
    <ul class="contact-list contact-phones">
      <li>
        <svg class="icon" viewBox="0 0 24 24"><path d="M6.6 10.8a15.1 15.1 0 0 0 6.6 6.6l2.2-2.2a1 1 0 0 1 1-.25 11.4 11.4 0 0 0 3.6.57 1 1 0 0 1 1 1V20a1 1 0 0 1-1 1A17 17 0 0 1 3 4a1 1 0 0 1 1-1h3.5a1 1 0 0 1 1 1c0 1.25.2 2.45.57 3.57a1 1 0 0 1-.25 1z"/></svg>
        <span>02 5550 1843</span>
      </li>
      <li>
        <svg class="icon" viewBox="0 0 24 24"><path d="M7 1h10a2 2 0 0 1 2 2v18a2 2 0 0 1-2 2H7a2 2 0 0 1-2-2V3a2 2 0 0 1 2-2zm0 3v14h10V4zm5 15.5a1.2 1.2 0 1 0 0 2.4 1.2 1.2 0 0 0 0-2.4z"/></svg>
        <span>0439 602 158</span>
      </li>
    </ul>
    <ul class="contact-list contact-online">
      <li>
        <span>gareth@1923basinsandspouts.com.au</span>
        <svg class="icon" viewBox="0 0 24 24"><path d="M2 5h20v14H2zm2 2v.4l8 5.2 8-5.2V7zm0 2.8V17h16V9.8l-8 5.2z"/></svg>
      </li>
      <li>
        <span>www.1923basinsandspouts.com.au</span>
        <svg class="icon" viewBox="0 0 24 24"><circle cx="12" cy="12" r="10"/><path d="M12 2v20M2 12h20" stroke="#fff" stroke-width="1.5" fill="none"/></svg>
      </li>
    </ul>
  </section>

  <section class="card card-back">
    <div class="back-brand">1923 Basins &amp; Spouts</div>
    <div class="back-web">www.1923basinsandspouts.com.au</div>
  </section>
</main>
</body>
</html>
```